Customs House descriptive business cards

We require a two-sided business card that has a simple yet elegant design. We want to be able to promote our services as a customs house. This card should include our logo, contact info and services offered with the logo being on one side and the contact info and services on the flip side

Target Market(s)

Importers / exporters to and from the Bahamas

Industry/Entity Type

Logistics

Contact Information for Business Card

The front side of the card could have the logo and the flip side should have the other relevant info

Font styles to use
Serif

Colors

Designer to choose colors to be used in the design.

Requirements
Must have
• (Harbourline Agents Ltd) Logo, address and contact info also services:
• import customs clearance, Delivery & HAndling services,Florida pickups, Export packing & Crating Services, export customs clearance, Consulting

```html
<!DOCTYPE html>
<html lang="en">
<head>
<meta charset="utf-8">
<title>Harbourline Agents Ltd – Business Card</title>
<link rel="stylesheet" href="https://fonts.googleapis.com/css2?family=EB+Garamond:wght@400;500;600&display=swap">
<style>
  :root {
    --backdrop: #8a8c8f;
    --backdrop-dark: #4a4c4f;
    --card: #1c1c1e;
    --card-deep: #111112;
    --card-edge: #2a2a2c;
    --accent: #2a9be0;
    --accent-bright: #3bb0f2;
    --ink: #ffffff;
    --ink-soft: #e6e6e6;
  }
  * { box-sizing: border-box; margin: 0; padding: 0; }
  html, body {
    width: 1200px;
    height: 1000px;
    overflow: hidden;
  }
  body {
    background: radial-gradient(ellipse at 50% 40%, var(--backdrop) 0%, var(--backdrop-dark) 100%);
    font-family: "EB Garamond", Georgia, serif;
    color: var(--ink);
    position: relative;
  }
  .card {
    position: absolute;
    left: 220px;
    width: 760px;
    height: 434px;
    border-radius: 26px;
    overflow: hidden;
    box-shadow: 0 18px 40px rgba(0,0,0,0.45);
  }
  .card--front { top: 46px; }
  .card--back {
    top: 520px;
    background: linear-gradient(135deg, var(--card-edge) 0%, var(--card) 45%, var(--card-deep) 100%);
  }

  /* Front */
  .front-texture {
    position: absolute;
    inset: 0;
    background: linear-gradient(135deg, #252527 0%, var(--card) 50%, #19191a 100%);
  }
  .front-brand {
    position: absolute;
    inset: 0;
    display: flex;
    align-items: center;
    justify-content: center;
  }
  .brand-name {
    font-size: 50px;
    font-weight: 500;
    letter-spacing: 1px;
    color: var(--accent);
  }

  /* Back */
  .contact {
    position: absolute;
    top: 70px;
    left: 0;
    right: 0;
    text-align: center;
  }
  .contact__name {
    font-size: 36px;
    font-weight: 500;
    color: var(--accent-bright);
    line-height: 1;
  }
  .contact__title {
    font-size: 20px;
    color: var(--ink);
    margin-left: 10px;
  }
  .contact__address {
    margin-top: 14px;
    font-size: 17px;
    color: var(--ink-soft);
  }
  .contact__lines {
    margin-top: 8px;
    font-size: 17px;
    color: var(--ink-soft);
    display: flex;
    justify-content: center;
    align-items: center;
    gap: 8px;
  }
  .contact__item { display: inline-flex; align-items: center; gap: 5px; }
  .icon { width: 13px; height: 13px; fill: var(--accent-bright); }
  .sep { color: var(--ink-soft); }
  .web-domain { color: var(--accent-bright); }

  .divider {
    position: absolute;
    top: 206px;
    left: 260px;
    width: 240px;
    height: 1px;
    background: var(--accent);
  }

  .services__heading {
    position: absolute;
    top: 228px;
    left: 0;
    right: 0;
    text-align: center;
    font-size: 17px;
    font-weight: 500;
    letter-spacing: 1px;
    color: var(--accent-bright);
  }
  .services {
    position: absolute;
    top: 262px;
    left: 0;
    right: 0;
    display: flex;
    justify-content: center;
    gap: 26px;
  }
  .services__col { list-style: none; }
  .services__col li {
    font-size: 18px;
    line-height: 30px;
    color: var(--ink);
    display: flex;
    align-items: center;
    gap: 10px;
  }
  .services__col--left li { justify-content: flex-end; }
  .bullet {
    width: 7px;
    height: 7px;
    background: var(--accent-bright);
    flex: none;
  }
</style>
</head>
<body>

  <section class="card card--front" aria-label="Card front">
    <div class="front-texture" role="img" aria-label="Faint dark tonal pattern of repeated brand marks"></div>
    <div class="front-brand">
      <h1 class="brand-name">Harbourline Agents Ltd</h1>
    </div>
  </section>

  <section class="card card--back" aria-label="Card back">
    <div class="contact">
      <p><span class="contact__name">Marcus Hale</span><span class="contact__title">President</span></p>
      <p class="contact__address">1450 W. Harbor View Dr. Suite 210, Larkfield 74310</p>
      <p class="contact__lines">
        <span class="contact__item">
          <svg class="icon" viewBox="0 0 16 16" aria-hidden="true"><path d="M3.6 1.2l2.3 2.6-1.4 1.8c.9 2 2.5 3.6 4.5 4.5l1.8-1.4 2.6 2.3-1.2 2.6C6.6 13.4 2.6 9.4 1 3.4z"/></svg>
          <span>600.555.0142</span>
        </span>
        <span class="sep">|</span>
        <span class="contact__item">
          <svg class="icon" viewBox="0 0 16 16" aria-hidden="true"><path d="M1 3h14v10H1z M2 4.2v.6l6 4 6-4v-.6z" fill-rule="evenodd"/></svg>
          <span>marcus@harbourlineagents.com</span>
        </span>
        <span class="sep">|</span>
        <span class="contact__item">
          <svg class="icon" viewBox="0 0 16 16" aria-hidden="true"><circle cx="8" cy="8" r="7"/><path d="M1 8h14M8 1c-3 3.5-3 10.5 0 14M8 1c3 3.5 3 10.5 0 14" stroke="#1c1c1e" stroke-width="1" fill="none"/></svg>
          <span>www.<span class="web-domain">harbourlineagents</span>.com</span>
        </span>
      </p>
    </div>

    <div class="divider"></div>

    <h2 class="services__heading">SERVICES OFFERED :</h2>
    <div class="services">
      <ul class="services__col services__col--left">
        <li>Import Customs Clearance<span class="bullet"></span></li>
        <li>Delivery &amp; HAndling Services<span class="bullet"></span></li>
        <li>Florida Pickups<span class="bullet"></span></li>
      </ul>
      <ul class="services__col services__col--right">
        <li><span class="bullet"></span>Export packing &amp; Crating Services</li>
        <li><span class="bullet"></span>Export Customs Clearance</li>
        <li><span class="bullet"></span>Consulting</li>
      </ul>
    </div>
  </section>

</body>
</html>
```